Effectively Manage Muscular Pain /with Remedial Massage

A flyer to sell remedial massage Therapy for muscular pain .

$10 Discount with this flyer

Use colors orange and Blak with the color of the logo provided and preferably the fonts as well .

Little spin about remedial massage:

Remedial massage is a deep massage , to create the conditions for the body’s return to normal health after injury or with muscular-skeletal disorders. It is used to treat chronic muscular-skeletal imbalances, strains, sprains, broken bones, bruising or any injury. Deep tissue massage removes blockages, damaged cells, scar tissue and adhesions [speeds up recovery Remedial massage is also used for conditions created by lifestyle for example Repetitive strain injury and Back pain.

Target Market(s)

young professionals with kids , modern suburban couples

Industry/Entity Type

Massage

Requirements
Must have
• doble sided.

Address 418 tindall Rd , Footscray Book Now 96402873

```html
<!DOCTYPE html>
<html lang="en">
<head>
<meta charset="utf-8">
<title>Marlo Health – Remedial Massage Flyer</title>
<link href="https://fonts.googleapis.com/css2?family=Noto+Serif:wght@400;700&family=Pathway+Gothic+One&display=swap" rel="stylesheet">
<style>
  :root {
    --charcoal: #322e2f;
    --orange: #f07a2a;
    --white: #ffffff;
    --ink: #111111;
    --red: #e0141b;
    --photo-grey: #bdbdbd;
    --photo-blue: #9fb6d8;
  }
  * { box-sizing: border-box; margin: 0; padding: 0; }
  html, body { width: 1200px; height: 901px; overflow: hidden; }
  body {
    background: linear-gradient(180deg, #d9d9d9 0%, #c9c9c9 100%);
    position: relative;
    font-family: "Noto Serif", Georgia, serif;
  }
  .flyer {
    position: absolute;
    width: 320px;
    height: 620px;
    background: var(--charcoal);
    box-shadow: 0 10px 24px rgba(0,0,0,.25);
    overflow: hidden;
  }
  .flyer--front { left: 150px; top: 90px; }
  .flyer--back { left: 520px; top: 60px; }

  .brand { display: flex; align-items: center; gap: 14px; }
  .brand__dot {
    width: 18px; height: 18px;
    border-radius: 50%;
    background: var(--orange);
    flex: none;
  }
  .brand__name {
    font-family: "Pathway Gothic One", "Arial Narrow", sans-serif;
    color: var(--white);
    text-transform: uppercase;
    letter-spacing: .5px;
    line-height: 1;
  }
  .flyer__header {
    height: 110px;
    padding-left: 28px;
    border-bottom: 4px solid var(--orange);
  }
  .flyer__header .brand__name { font-size: 26px; }

  .photo { height: 210px; border-bottom: 4px solid var(--orange); }
  .photo--back-pain {
    background: radial-gradient(circle at 50% 75%, rgba(240,90,80,.45) 0 14%, transparent 30%),
                linear-gradient(180deg, #f4f4f4 0%, var(--photo-grey) 60%, #6f6f6f 100%);
  }
  .photo--neck-pain {
    background: radial-gradient(ellipse at 58% 70%, var(--photo-blue) 0 30%, transparent 55%),
                linear-gradient(180deg, #ffffff 0%, #eeeeee 100%);
  }

  .flyer__copy {
    padding: 26px 24px 0;
    color: #e8e8e8;
    font-size: 12px;
    line-height: 1.55;
  }

  .booking { padding: 34px 0 0 30px; color: var(--white); }
  .booking__label { font-size: 24px; font-weight: 700; line-height: 1; }
  .booking__phone {
    font-size: 40px; font-weight: 700; line-height: 1.05;
    padding-left: 58px; letter-spacing: 1px;
  }
  .coupon {
    margin: 14px 0 0 80px;
    width: 190px; height: 64px;
    background: var(--white);
    transform: rotate(-3deg);
    display: flex; align-items: center; gap: 6px;
    padding-left: 14px;
    color: var(--ink);
  }
  .coupon__amount { font-size: 38px; font-weight: 700; line-height: 1; }
  .coupon__amount sup { font-size: 20px; }
  .coupon__terms { font-size: 13px; line-height: 1; }
  .coupon__discount { color: var(--red); font-weight: 700; font-size: 15px; display: block; }

  .address {
    position: absolute; left: 200px; top: 528px;
    color: #dddddd; font-size: 12px; line-height: 1.5;
  }
  .flyer__footer { position: absolute; left: 26px; bottom: 26px; }
  .flyer__footer .brand__name { font-size: 22px; }

  .brand-card {
    position: absolute;
    left: 703px; top: 712px;
    width: 452px; height: 146px;
    background: var(--charcoal);
    padding-left: 44px;
    display: flex; align-items: center;
  }
  .brand-card .brand { gap: 28px; }
  .brand-card .brand__dot { width: 40px; height: 40px; }
  .brand-card .brand__name { font-size: 44px; }
</style>
</head>
<body>

  <section class="flyer flyer--front">
    <header class="flyer__header brand">
      <span class="brand__dot"></span>
      <span class="brand__name">Marlo Health</span>
    </header>
    <div class="photo photo--back-pain" role="img" aria-label="Black and white photo of a woman holding her lower back, the painful area glowing red"></div>
    <p class="flyer__copy">Remedial massage is a deep massage , to create the conditions for the body's return to normal health after injury or with muscular-skeletal disorders. It is used to treat chronic muscular-skeletal imbalances, strains, sprains, broken bones, bruising or any injury. Deep tissue massage removes blockages, damaged cells, scar tissue and adhesions [speeds up recovery Remedial massage is also used for conditions created by lifestyle for example Repetitive strain injury and Back pain</p>
  </section>

  <section class="flyer flyer--back">
    <header class="flyer__header brand">
      <span class="brand__dot"></span>
      <span class="brand__name">Marlo Health</span>
    </header>
    <div class="photo photo--neck-pain" role="img" aria-label="Photo of a woman in a blue shirt at her desk rubbing her sore neck"></div>
    <div class="booking">
      <p class="booking__label">Book Now</p>
      <p class="booking__phone">96402873</p>
      <div class="coupon">
        <span class="coupon__amount"><sup>$</sup>10</span>
        <span class="coupon__terms"><span class="coupon__discount">DISCOUNT</span>with this flyer</span>
      </div>
    </div>
    <p class="address">418 tindall Rd ,<br>Footscray</p>
    <footer class="flyer__footer">
      <div class="brand">
        <span class="brand__dot"></span>
        <span class="brand__name">Marlo Health</span>
      </div>
    </footer>
  </section>

  <div class="brand-card">
    <div class="brand">
      <span class="brand__dot"></span>
      <span class="brand__name">Marlo Health</span>
    </div>
  </div>

</body>
</html>
```